Design revision of an existing Executive Summary

Our company velmora is specialized in the field of performance engineering (load and performance testing as well as application performance monitoring). We are looking for a designer who could graphically "spice up" our current executive summary about our company velmora (www.velmora-it.example). Maybe it would be possible to incorporate a pic of our website (e.g. https://www.velmora-it.example/en/services/performance/) into this newly designed executive summary.

Attached you will find the current executive summary which should not change textually. It should just look fresher and more modern. Ideally, a visually appealing first / title page would precede the text.

```html
<!DOCTYPE html>
<html lang="en">
<head>
<meta charset="utf-8">
<title>velmora – Executive Summary</title>
<link rel="stylesheet" href="https://fonts.googleapis.com/css2?family=Comfortaa:wght@300&family=Roboto:wght@300;400;700&display=swap">
<style>
  :root {
    --stage: #2e2e30;
    --sheet: #444447;
    --sheet-deep: #3b3b3e;
    --accent: #67c8e8;
    --accent-text: #5ec4ea;
    --ink-dark: #2a2a2c;
    --ink-light: #f2f2f2;
    --ink-soft: #dcdcdc;
    --hex: #333336;
    --photo-a: #0b1a2c;
    --photo-b: #1f5f8c;
    --photo-c: #2a2d35;
  }
  * { margin: 0; padding: 0; box-sizing: border-box; }
  html, body { width: 783px; height: 1200px; overflow: hidden; }
  body {
    background: var(--stage);
    font-family: "Roboto", Arial, sans-serif;
    position: relative;
  }
  .brochure {
    position: absolute;
    width: 672px;
    height: 518px;
    background: linear-gradient(90deg, var(--sheet) 0%, var(--sheet-deep) 33%, var(--sheet) 34%, var(--sheet-deep) 66%, var(--sheet) 67%, var(--sheet-deep) 100%);
    overflow: hidden;
  }
  .brochure--upper { left: 66px; top: 42px; }
  .brochure--lower { left: 63px; top: 649px; }

  .brand-wordmark {
    position: absolute; left: 56px; top: 34px;
    font-family: "Comfortaa", sans-serif; font-weight: 300;
    font-size: 34px; line-height: 40px; color: var(--ink-light); letter-spacing: 1px;
  }
  .hero-visual {
    position: absolute; left: 0; top: 86px; width: 222px; height: 284px;
    border-radius: 150px 60px 0 0;
    background: radial-gradient(circle at 58% 55%, var(--photo-b) 0%, var(--photo-a) 45%, var(--photo-c) 100%);
  }
  .hero-title {
    position: absolute; left: 20px; top: 352px;
    font-weight: 700; font-size: 37px; line-height: 40px; color: var(--accent-text); letter-spacing: -0.5px;
  }
  .hero-subtitle {
    position: absolute; left: 27px; top: 393px;
    font-weight: 700; font-size: 11px; color: var(--ink-light); letter-spacing: 0.3px;
  }
  .hero-rule { position: absolute; left: 27px; top: 413px; width: 36px; height: 2px; background: var(--accent); }
  .hero-tagline {
    position: absolute; left: 27px; top: 422px; width: 175px;
    font-size: 10px; line-height: 12px; color: var(--ink-light);
  }
  .hero-url {
    position: absolute; left: 28px; top: 464px; width: 171px; height: 19px;
    border-radius: 10px; background: #39393c;
    display: flex; align-items: center; gap: 8px; padding-left: 12px;
    font-size: 11px; color: var(--accent-text); white-space: nowrap;
  }

  .section-bar {
    position: absolute; height: 20px; width: 173px;
    background: var(--accent);
    font-weight: 700; font-size: 12px; color: var(--ink-dark);
    padding-left: 16px; line-height: 21px;
  }
  .body-copy {
    position: absolute;
    font-weight: 300; font-size: 8.4px; line-height: 9.3px; color: var(--ink-soft);
  }
  .team-copy--left { left: 238px; top: 56px; width: 192px; }
  .team-copy--right { left: 463px; top: 70px; width: 194px; }

  .service { position: absolute; left: 238px; width: 200px; }
  .service-hex { position: absolute; left: 0; top: 2px; width: 36px; height: 40px; }
  .service-title {
    position: absolute; left: 46px; top: 0;
    font-size: 11px; font-weight: 400; color: var(--accent-text); white-space: nowrap;
  }
  .service-copy { position: absolute; left: 46px; top: 14px; width: 152px; }

  .customer-list { position: absolute; left: 463px; top: 232px; width: 170px; height: 140px; }
  .customer-name {
    position: absolute; font-weight: 700; font-size: 13px; color: var(--ink-light); white-space: nowrap;
  }

  .contact-list { position: absolute; left: 463px; top: 425px; list-style: none; }
  .contact-item {
    display: flex; align-items: center; gap: 10px; height: 15.6px;
    font-size: 7.5px; color: var(--ink-light); white-space: nowrap;
  }
  .contact-item svg { width: 10px; height: 10px; flex: none; }
</style>
</head>
<body>

<article class="brochure brochure--upper">
  <div class="brand-wordmark">velmora</div>
  <div class="hero-visual" role="img" aria-label="Photo of an open hand holding a glowing blue check mark surrounded by circular tech icons"></div>
  <h1 class="hero-title">VELMORA</h1>
  <p class="hero-subtitle">LOAD &amp; PERFORMANCE TEST</p>
  <span class="hero-rule"></span>
  <p class="hero-tagline">Your service provider for application performance</p>
  <div class="hero-url">
    <svg width="11" height="11" viewBox="0 0 12 12" fill="none" stroke="#5ec4ea" stroke-width="1"><circle cx="6" cy="6" r="5"/><ellipse cx="6" cy="6" rx="2.2" ry="5"/><line x1="1" y1="6" x2="11" y2="6"/></svg>
    <span>www.velmora-it.example</span>
  </div>

  <h2 class="section-bar" style="left:224px;top:16px;">OUR TEAM</h2>
  <p class="body-copy team-copy--left">Velmora is the go-to-company in the very specialized area of performance engineering. Whether microser­vices in the cloud or legacy on-premise: We will show you the added value of load &amp; performance tests, performance tuning or monitoring solutions. In the area of application performance monitoring, we like to work with the enterprise solution from industry leader Observa. velmora is Observa Premier Partner and therefore amongst an exclusive group of companies in the EMEA region specialized in Observa.</p>

  <h2 class="section-bar" style="left:224px;top:176px;">OUR SERVICES</h2>

  <section class="service" style="top:212px;">
    <svg class="service-hex" viewBox="0 0 36 40"><polygon points="18,1 35,10 35,30 18,39 1,30 1,10" fill="var(--hex)"/><rect x="10" y="13" width="16" height="11" rx="1" fill="none" stroke="#5ec4ea" stroke-width="1.4"/><line x1="18" y1="24" x2="18" y2="28" stroke="#5ec4ea" stroke-width="1.4"/><line x1="14" y1="28" x2="22" y2="28" stroke="#5ec4ea" stroke-width="1.4"/></svg>
    <h3 class="service-title">Load &amp; Performance Testing</h3>
    <p class="body-copy service-copy">An often-neglected necessity to ensure the speed, stability and reliability of your IT applications and digital services. If you expect many users rushing in on your digital roads, performance tests are required to provide the best experience for your customers.</p>
  </section>
  <section class="service" style="top:306px;">
    <svg class="service-hex" viewBox="0 0 36 40"><polygon points="18,1 35,10 35,30 18,39 1,30 1,10" fill="var(--hex)"/><circle cx="18" cy="15" r="4" fill="none" stroke="#5ec4ea" stroke-width="1.4"/><rect x="9" y="23" width="5" height="6" fill="#5ec4ea"/><rect x="16" y="23" width="5" height="6" fill="#5ec4ea"/><rect x="23" y="23" width="5" height="6" fill="#5ec4ea"/></svg>
    <h3 class="service-title">APM &amp; Observability</h3>
    <p class="body-copy service-copy">Follow the experience of users and pinpoint the root-cause of problems as fast as possible in case of an undesired event and get business insights like usage statistics and conversion rates just along the way.</p>
  </section>
  <section class="service" style="top:391px;">
    <svg class="service-hex" viewBox="0 0 36 40"><polygon points="18,1 35,10 35,30 18,39 1,30 1,10" fill="var(--hex)"/><rect x="11" y="11" width="15" height="9" fill="none" stroke="#5ec4ea" stroke-width="1.4"/><circle cx="13" cy="24" r="2" fill="#5ec4ea"/><circle cx="23" cy="24" r="2" fill="#5ec4ea"/><rect x="10" y="27" width="6" height="3" fill="#5ec4ea"/><rect x="20" y="27" width="6" height="3" fill="#5ec4ea"/></svg>
    <h3 class="service-title">Trainings &amp; Workshops</h3>
    <p class="body-copy service-copy">Enable your own performance testing team by learning innovative approaches such as the automation of quality gates and automate performance feedback or get started with the basic methodology training.</p>
  </section>

  <h2 class="section-bar" style="left:446px;top:36px;">OUR TEAM</h2>
  <p class="body-copy team-copy--right">Our performance engineers guide our customers through the whole process of performance testing by providing best practices for test design and test strategies, setting up infrastructure, carrying out performance tests as well as preparing the reporting. If required, our performance engineers go beyond reporting by identifying the actual bottlenecks and even performing code reviews. As we offer to play such an active role in fixing performance defects, all our consultants are well-skilled software engineers.</p>

  <h2 class="section-bar" style="left:448px;top:200px;">VALUED CUSTOMERS</h2>
  <div class="customer-list">
    <span class="customer-name" style="left:0;top:10px;">NORDVEST</span>
    <span class="customer-name" style="left:92px;top:10px;">BRANDHOLM</span>
    <span class="customer-name" style="left:0;top:48px;">ALTMERA</span>
    <span class="customer-name" style="left:92px;top:48px;">ORTISA</span>
    <span class="customer-name" style="left:92px;top:82px;">KAMERO</span>
    <span class="customer-name" style="left:0;top:82px;">GEMVERA</span>
  </div>

  <h2 class="section-bar" style="left:448px;top:387px;">CONTACT US</h2>
  <ul class="contact-list">
    <li class="contact-item"><svg viewBox="0 0 10 10"><path d="M2 1 L4 1 L4.6 3 L3.4 4 Q4.5 6 6 6.6 L7 5.4 L9 6 L9 8 Q8 9 6.5 8.6 Q2.5 7 1.4 3 Q1 1.8 2 1Z" fill="#5ec4ea"/></svg>+43 - 1 - 55 01 23 0000</li>
    <li class="contact-item"><svg viewBox="0 0 10 10" fill="none" stroke="#5ec4ea" stroke-width="0.9"><circle cx="5" cy="5" r="4.2"/><ellipse cx="5" cy="5" rx="1.8" ry="4.2"/><line x1="0.8" y1="5" x2="9.2" y2="5"/></svg>www.velmora-it.example</li>
    <li class="contact-item"><svg viewBox="0 0 10 10" fill="none" stroke="#5ec4ea" stroke-width="0.9"><rect x="0.8" y="2" width="8.4" height="6"/><polyline points="0.8,2 5,5.5 9.2,2"/></svg>office@velmora-it.example</li>
    <li class="contact-item"><svg viewBox="0 0 10 10"><rect x="1" y="1" width="8" height="8" rx="1" fill="#5ec4ea"/></svg>www.socialnet.example/company/velmora</li>
  </ul>
</article>

<article class="brochure brochure--lower">
  <div class="brand-wordmark">velmora</div>
  <div class="hero-visual" role="img" aria-label="Photo of an open hand holding a glowing blue check mark surrounded by circular tech icons"></div>
  <h1 class="hero-title">VELMORA</h1>
  <p class="hero-subtitle">LOAD &amp; PERFORMANCE TEST</p>
  <span class="hero-rule"></span>
  <p class="hero-tagline">Your service provider for application performance</p>
  <div class="hero-url">
    <svg width="11" height="11" viewBox="0 0 12 12" fill="none" stroke="#5ec4ea" stroke-width="1"><circle cx="6" cy="6" r="5"/><ellipse cx="6" cy="6" rx="2.2" ry="5"/><line x1="1" y1="6" x2="11" y2="6"/></svg>
    <span>www.velmora-it.example</span>
  </div>

  <h2 class="section-bar" style="left:224px;top:16px;">OUR TEAM</h2>
  <p class="body-copy team-copy--left">Velmora is the go-to-company in the very specialized area of performance engineering. Whether microser­vices in the cloud or legacy on-premise: We will show you the added value of load &amp; performance tests, performance tuning or monitoring solutions. In the area of application performance monitoring, we like to work with the enterprise solution from industry leader Observa. velmora is Observa Premier Partner and therefore amongst an exclusive group of companies in the EMEA region specialized in Observa.</p>

  <h2 class="section-bar" style="left:224px;top:176px;">OUR SERVICES</h2>

  <section class="service" style="top:212px;">
    <svg class="service-hex" viewBox="0 0 36 40"><polygon points="18,1 35,10 35,30 18,39 1,30 1,10" fill="var(--hex)"/><rect x="10" y="13" width="16" height="11" rx="1" fill="none" stroke="#5ec4ea" stroke-width="1.4"/><line x1="18" y1="24" x2="18" y2="28" stroke="#5ec4ea" stroke-width="1.4"/><line x1="14" y1="28" x2="22" y2="28" stroke="#5ec4ea" stroke-width="1.4"/></svg>
    <h3 class="service-title">Load &amp; Performance Testing</h3>
    <p class="body-copy service-copy">An often-neglected necessity to ensure the speed, stability and reliability of your IT applications and digital services. If you expect many users rushing in on your digital roads, performance tests are required to provide the best experience for your customers.</p>
  </section>
  <section class="service" style="top:306px;">
    <svg class="service-hex" viewBox="0 0 36 40"><polygon points="18,1 35,10 35,30 18,39 1,30 1,10" fill="var(--hex)"/><circle cx="18" cy="15" r="4" fill="none" stroke="#5ec4ea" stroke-width="1.4"/><rect x="9" y="23" width="5" height="6" fill="#5ec4ea"/><rect x="16" y="23" width="5" height="6" fill="#5ec4ea"/><rect x="23" y="23" width="5" height="6" fill="#5ec4ea"/></svg>
    <h3 class="service-title">APM &amp; Observability</h3>
    <p class="body-copy service-copy">Follow the experience of users and pinpoint the root-cause of problems as fast as possible in case of an undesired event and get business insights like usage statistics and conversion rates just along the way.</p>
  </section>
  <section class="service" style="top:391px;">
    <svg class="service-hex" viewBox="0 0 36 40"><polygon points="18,1 35,10 35,30 18,39 1,30 1,10" fill="var(--hex)"/><rect x="11" y="11" width="15" height="9" fill="none" stroke="#5ec4ea" stroke-width="1.4"/><circle cx="13" cy="24" r="2" fill="#5ec4ea"/><circle cx="23" cy="24" r="2" fill="#5ec4ea"/><rect x="10" y="27" width="6" height="3" fill="#5ec4ea"/><rect x="20" y="27" width="6" height="3" fill="#5ec4ea"/></svg>
    <h3 class="service-title">Trainings &amp; Workshops</h3>
    <p class="body-copy service-copy">Enable your own performance testing team by learning innovative approaches such as the automation of quality gates and automate performance feedback or get started with the basic methodology training.</p>
  </section>

  <h2 class="section-bar" style="left:446px;top:36px;">OUR TEAM</h2>
  <p class="body-copy team-copy--right">Our performance engineers guide our customers through the whole process of performance testing by providing best practices for test design and test strategies, setting up infrastructure, carrying out performance tests as well as preparing the reporting. If required, our performance engineers go beyond reporting by identifying the actual bottlenecks and even performing code reviews. As we offer to play such an active role in fixing performance defects, all our consultants are well-skilled software engineers.</p>

  <h2 class="section-bar" style="left:448px;top:200px;">VALUED CUSTOMERS</h2>
  <div class="customer-list">
    <span class="customer-name" style="left:0;top:10px;">NORDVEST</span>
    <span class="customer-name" style="left:92px;top:10px;">BRANDHOLM</span>
    <span class="customer-name" style="left:0;top:48px;">ALTMERA</span>
    <span class="customer-name" style="left:92px;top:48px;">ORTISA</span>
    <span class="customer-name" style="left:92px;top:82px;">KAMERO</span>
    <span class="customer-name" style="left:0;top:82px;">GEMVERA</span>
  </div>

  <h2 class="section-bar" style="left:448px;top:387px;">CONTACT US</h2>
  <ul class="contact-list">
    <li class="contact-item"><svg viewBox="0 0 10 10"><path d="M2 1 L4 1 L4.6 3 L3.4 4 Q4.5 6 6 6.6 L7 5.4 L9 6 L9 8 Q8 9 6.5 8.6 Q2.5 7 1.4 3 Q1 1.8 2 1Z" fill="#5ec4ea"/></svg>+43 - 1 - 55 01 23 0000</li>
    <li class="contact-item"><svg viewBox="0 0 10 10" fill="none" stroke="#5ec4ea" stroke-width="0.9"><circle cx="5" cy="5" r="4.2"/><ellipse cx="5" cy="5" rx="1.8" ry="4.2"/><line x1="0.8" y1="5" x2="9.2" y2="5"/></svg>www.velmora-it.example</li>
    <li class="contact-item"><svg viewBox="0 0 10 10" fill="none" stroke="#5ec4ea" stroke-width="0.9"><rect x="0.8" y="2" width="8.4" height="6"/><polyline points="0.8,2 5,5.5 9.2,2"/></svg>office@velmora-it.example</li>
    <li class="contact-item"><svg viewBox="0 0 10 10"><rect x="1" y="1" width="8" height="8" rx="1" fill="#5ec4ea"/></svg>www.socialnet.example/company/velmora</li>
  </ul>
</article>

</body>
</html>
```